R.T. Wexmoor Electrical work flyer

I need a flyer design to help generate some extra work. I'm more than happy for a designer to play around with pictures, text, headings, boarders. The flyer will be double sided A4 size.
We specialize in Residential, Commercial, & Industrial Electrical works including PV Solar System Designs & Installations, Maintenance, System Checks & Upgrades, Mains Upgrades, Overhead & Underground, Switchboard Installations & Upgrades, Safety Switches, Spa & Pool connections, LED Lighting solutions, Energy Audit Checks, Fans & Air Conditioning, Hi-bay Lighting, Carpark Lighting, Data Points, Comms Racks, New Home Builds, Office Fitouts ...
We pride ourselves on always doing a great job, guaranteed workmanship, competitive pricing, & leaving the site clean.
Call Derek for a quote on any of your electrical needs
Mobile:0418 736 204
Email: rtwexmoorelectrical@quillmail.test
PO Box 58
Brambleton Vale VIC 3179

LEN: 38517
NRB Accreditation: A3182609

I've added my company logo & some pics, photo's & electrical / solar brand logos that can be used but not a must. I'm more than happy if you can find better pics.

Target Market(s)

Office, Factory & Home Owners

Industry/Entity Type

Electrical

Font styles to use
Serif
Sans Serif

Requirements
Must have
• eye catchy design with not to much information overload.
• Just aiming for people to call up for quotes etc.
Nice to have
• My company logo, electrical & solar works available
Should not have
• pictures of kids

```html
<!DOCTYPE html>
<html lang="en">
<head>
<meta charset="utf-8">
<title>R.T. Wexmoor Electrical – Flyer</title>
<link rel="stylesheet" href="https://fonts.googleapis.com/css2?family=Arimo:wght@400;700&family=Exo+2:wght@400;500&family=Roboto+Condensed:wght@700&display=swap">
<style>
  :root {
    --green: #5cc62c;
    --green-text: #2f9a17;
    --ink: #2b2b2b;
    --ink-soft: #3a3a3a;
    --list-ink: #1e3412;
    --footer: #2d2d2d;
    --paper: #ffffff;
    --paper-grey: #e4e6e7;
  }
  * { margin: 0; padding: 0; box-sizing: border-box; }
  html, body { width: 825px; height: 1200px; overflow: hidden; background: var(--paper); }
  .flyer {
    position: relative; width: 825px; height: 1200px; overflow: hidden;
    background: linear-gradient(180deg, var(--paper) 0%, #f4f5f5 45%, var(--paper-grey) 100%);
    font-family: "Exo 2", sans-serif; color: var(--ink);
  }
  .shapes { position: absolute; inset: 0; }

  .brand {
    position: absolute; left: 424px; top: 54px;
    display: flex; align-items: center; gap: 16px;
  }
  .brand-dot { width: 62px; height: 62px; border-radius: 50%; background: var(--green); flex: none; }
  .brand-name {
    font-family: "Arimo", sans-serif; font-weight: 400; font-size: 33px; line-height: 1.1;
    color: var(--ink-soft); letter-spacing: 1px; white-space: nowrap;
  }

  .tagline {
    position: absolute; right: 44px; top: 168px; text-align: right; white-space: nowrap;
    font-family: "Arimo", sans-serif; font-size: 19.5px; line-height: 1.25; color: var(--ink-soft);
  }

  .services { position: absolute; right: 40px; top: 400px; text-align: right; color: #fff; }
  .services-title { font-family: "Arimo", sans-serif; font-weight: 700; font-size: 28px; margin-right: 2px; margin-bottom: 8px; }
  .services-lead { font-size: 18.5px; line-height: 1.3; margin-bottom: 14px; color: #1f3a12; }
  .services-lead span::after { content: " <<"; color: #fff; }
  .services-list { list-style: none; font-size: 18.5px; line-height: 31.5px; color: var(--list-ink); }
  .services-list li::after,
  .services-list .line::after {
    content: ""; display: inline-block; width: 11px; height: 11px; border-radius: 50%;
    background: #fff; margin-left: 10px; vertical-align: 1px;
  }
  .services-list li.two-line::after { display: none; }
  .services-list li.two-line { line-height: 22px; padding: 5px 0; }
  .services-list .cont { margin-right: 21px; }

  .promise { position: absolute; left: 38px; top: 610px; }
  .promise-lead { font-family: "Roboto Condensed", sans-serif; font-weight: 700; font-size: 30px; color: var(--green-text); }
  .promise-main { font-family: "Arimo", sans-serif; font-size: 40px; color: var(--ink); margin-top: -2px; }

  .quote { position: absolute; left: 38px; top: 730px; font-family: "Arimo", sans-serif; font-weight: 700; }
  .quote-call { font-size: 30px; color: #fff; }
  .quote-phone { font-size: 28px; color: #1c1c1c; margin-top: 4px; }

  .bulb-art {
    position: absolute; left: 42px; top: 850px; width: 330px; height: 165px;
    border-radius: 40px 90px 90px 40px / 40px 82px 82px 40px;
    background: radial-gradient(ellipse at 65% 40%, #bfe3f7 0%, #4a8fc9 45%, #1d4f86 80%, #6c7378 100%);
  }

  .licences { position: absolute; left: 38px; top: 1062px; font-family: "Arimo", sans-serif; font-size: 14.5px; line-height: 19px; color: var(--green-text); }

  .footer {
    position: absolute; left: 0; right: 0; bottom: 0; height: 58px; background: var(--footer);
    border-top: 7px solid var(--green);
    color: #fff; font-family: "Arimo", sans-serif; font-size: 14px;
    display: flex; align-items: center; justify-content: center; gap: 6px;
  }
  .footer b { font-weight: 700; }
</style>
</head>
<body>
<main class="flyer">
  <svg class="shapes" width="825" height="1200" viewBox="0 0 825 1200" aria-hidden="true">
    <defs>
      <linearGradient id="panelFill" x1="0" y1="0" x2="0.3" y2="1">
        <stop offset="0" stop-color="#9be85a"/>
        <stop offset="0.55" stop-color="#6fd23a"/>
        <stop offset="1" stop-color="#44b822"/>
      </linearGradient>
      <linearGradient id="bandFill" x1="0" y1="0" x2="0" y2="1">
        <stop offset="0" stop-color="#7fd948"/>
        <stop offset="1" stop-color="#3faf1f"/>
      </linearGradient>
      <linearGradient id="photoFill" x1="0" y1="0" x2="0" y2="1">
        <stop offset="0" stop-color="#8fc3ea"/>
        <stop offset="0.28" stop-color="#a9b6c0"/>
        <stop offset="0.4" stop-color="#2c3f7a"/>
        <stop offset="0.75" stop-color="#24366c"/>
        <stop offset="1" stop-color="#b9c2c8"/>
      </linearGradient>
    </defs>

    <!-- service panel -->
    <path d="M418 362 Q620 326 825 338 L825 1144 L292 1144 Q350 800 418 362 Z" fill="url(#panelFill)"/>
    <!-- top sweep with arrow -->
    <path d="M408 358 Q600 312 790 322" fill="none" stroke="var(--green)" stroke-width="7"/>
    <path d="M414 367 Q600 327 780 331" fill="none" stroke="#fff" stroke-width="4"/>
    <polygon points="770,302 824,328 770,352" fill="#fff"/>
    <!-- left sweep with arrow -->
    <path d="M410 370 Q345 800 308 1100" fill="none" stroke="#fff" stroke-width="9"/>
    <polygon points="284,1090 330,1094 292,1130" fill="#fff"/>

    <!-- quote band -->
    <rect x="0" y="712" width="436" height="116" fill="url(#bandFill)"/>
    <rect x="0" y="706" width="436" height="4" fill="#9a9a9a"/>
    <rect x="0" y="830" width="436" height="4" fill="#9a9a9a"/>

    <!-- photo ring -->
    <circle cx="183" cy="291" r="238" fill="none" stroke="var(--green)" stroke-width="10"/>
    <polygon points="272,486 326,514 268,540" fill="var(--green)"/>
  </svg>

  <svg class="shapes" width="825" height="1200" viewBox="0 0 825 1200" role="img" aria-label="Photo of rows of solar panels on a factory roof under a blue sky">
    <circle cx="183" cy="291" r="226" fill="url(#photoFill)"/>
  </svg>

  <div class="brand">
    <span class="brand-dot"></span>
    <span class="brand-name">R.T. Wexmoor<br>Electrical</span>
  </div>

  <p class="tagline">We pride ourselves on always<br>doing a great job, guaranteed<br>workmanship, competitive pricing,<br>&amp; leaving the site clean.</p>

  <section class="services">
    <h2 class="services-title">We specialize in</h2>
    <p class="services-lead"><span>Residential, Commercial</span><br><span>&amp; Industrial Electrical works</span></p>
    <ul class="services-list">
      <li class="two-line"><span class="line">PV Solar System Designs</span><br><span class="cont">&amp; Installations</span></li>
      <li>Maintenance</li>
      <li>System Checks &amp; Upgrades</li>
      <li>Mains Upgrades</li>
      <li>Overhead &amp; Underground</li>
      <li class="two-line"><span class="line">Switchboard Installations</span><br><span class="cont">&amp; Upgrades</span></li>
      <li>Safety Switches</li>
      <li>Spa &amp; Pool connections</li>
      <li>LED Lighting solutions Energy</li>
      <li>Audit Checks</li>
      <li>Fans &amp; Air Conditioning</li>
      <li>Hi-bay Lighting</li>
      <li>Carpark Lighting</li>
      <li>Data Points</li>
      <li>Comms Racks</li>
      <li>New Home Builds</li>
      <li>Office Fitouts</li>
    </ul>
  </section>

  <div class="promise">
    <p class="promise-lead">Guaranteed workmanship</p>
    <p class="promise-main">Competitive pricing</p>
  </div>

  <div class="quote">
    <p class="quote-call">Call Derek for a quote</p>
    <p class="quote-phone">Mobile:0418 736 204</p>
  </div>

  <div class="bulb-art" role="img" aria-label="Illustration of a light bulb filled with solar panels, sky and clouds"></div>

  <p class="licences">LEN: 38517<br>NRB Accreditation: A3182609</p>

  <footer class="footer">
    <span><b>Email:</b> rtwexmoorelectrical@quillmail.test</span> |
    <span>PO Box 58 Brambleton Vale VIC 3179</span> |
    <span>Visit : www.rtwexmoorelectrical.test</span>
  </footer>
</main>
</body>
</html>
```